Silver Arch Consulting Website Design

I already have a live website. Just want some help with design, finishing up the project. I also have another site with wix that I am ready to have designed. I am not completely sure on the pages but will for sure need "coaching", "training", "resources". Most of the people I currently work with are real estate brokers and mortgage brokers but I want to be able to appeal to all industries.
Number of Pages Required
4 page
Font styles to use
Sans Serif
Colors
Requirements
Must have
- place holders for video
Nice to have
- a way for people to purchase digital downloads

```html
<!DOCTYPE html>
<html lang="en">
<head>
<meta charset="utf-8">
<title>Silver Arch Consulting</title>
<link href="https://fonts.googleapis.com/css2?family=Montserrat:wght@400;500;600;700&family=Josefin+Sans:ital,wght@0,400;0,600;1,400&display=swap" rel="stylesheet">
<style>
:root{
  --red:#e0271a;
  --red-deep:#d42014;
  --ink:#1d1d1d;
  --text:#3a3a3a;
  --muted:#6d6d6d;
  --line:#dcdcdc;
  --card-grey:#efefef;
  --dark:#1c1c1c;
  --white:#ffffff;
  --sans:'Montserrat',sans-serif;
  --alt:'Josefin Sans',sans-serif;
}
*{box-sizing:border-box;margin:0;padding:0}
html,body{width:1200px;height:3564px;overflow:hidden}
body{position:relative;background:var(--white);font-family:var(--sans);color:var(--text)}
.abs{position:absolute}

/* nav */
.site-nav{left:0;top:0;width:1200px;height:48px;background:var(--white)}
.brand{left:67px;top:12px;font-weight:700;font-size:17px;color:var(--red);display:flex;align-items:center;gap:8px}
.brand-dot{width:14px;height:14px;background:var(--red)}
.nav-links{right:102px;top:17px;display:flex;gap:30px;font-size:13px;font-weight:500;color:var(--ink);letter-spacing:.5px}

/* hero */
.hero{left:0;top:48px;width:1200px;height:627px;background:linear-gradient(120deg,#2b2b2b 0%,#161616 45%,#2a2a2a 75%,#1a1a1a 100%)}
.hero-title{left:549px;top:295px;font-size:43px;font-weight:700;color:var(--white);letter-spacing:1px}
.hero-text{left:549px;top:362px;width:520px;font-size:14.5px;font-style:italic;color:var(--white);line-height:22px}
.btn{background:var(--red);color:var(--white);font-weight:700;text-align:center;letter-spacing:.5px}
.hero-btn{left:549px;top:468px;width:202px;height:55px;line-height:55px;font-size:19px}

/* welcome */
.welcome-kicker{left:60px;top:795px;width:250px;text-align:right;font-family:var(--alt);font-style:italic;font-size:20px;color:var(--ink)}
.welcome-name{left:60px;top:828px;width:250px;text-align:right;font-size:15px;font-weight:700;color:var(--red)}
.welcome-text{left:65px;top:872px;width:245px;text-align:right;font-size:11px;line-height:18px;color:var(--text)}
.offer{width:240px;height:270px;top:744px;border:1px solid #e6e6e6;background:var(--white);padding:90px 18px 0}
.offer.is-featured{background:var(--card-grey)}
.offer-icon{position:absolute;left:92px;top:24px;width:56px;height:56px;border-radius:50%}
.offer h3{font-size:13px;font-weight:700;letter-spacing:.6px;color:var(--ink);line-height:19px}
.offer p{margin-top:10px;font-size:10.5px;line-height:14px;color:var(--text)}

/* about */
.about-panel{left:0;top:1086px;width:601px;height:399px;background:var(--red-deep)}
.about-title{left:0;top:1130px;width:601px;text-align:center;font-size:32px;font-weight:700;color:var(--white)}
.about-rule{left:273px;top:1187px;width:62px;height:3px;background:var(--white)}
.about-text{left:83px;top:1212px;width:480px;font-size:14.5px;line-height:30px;color:var(--white);font-weight:500}
.about-btn{left:83px;top:1395px;width:131px;height:37px;line-height:35px;border:2px solid var(--white);color:var(--white);text-align:center;font-weight:700;font-size:17px}
.about-video{left:601px;top:1086px;width:599px;height:399px;background:linear-gradient(100deg,#cfd3d6 0%,#a9a39c 40%,#6e6a66 70%,#2f3033 100%)}
.play{left:872px;top:1262px;width:64px;height:44px;border-radius:10px;background:var(--red)}

/* services */
.section-title{left:0;width:1200px;text-align:center;font-size:33px;font-weight:600;color:var(--ink)}
.section-title span{color:var(--red)}
.service{top:1672px;width:240px}
.service-icon{width:58px;height:58px;border-radius:50%}
.service h3{margin-top:28px;font-size:15px;font-weight:700;line-height:29px;letter-spacing:.4px;color:var(--ink)}
.service h3.is-active{color:var(--red)}
.service p{margin-top:12px;font-size:12.5px;line-height:24px;color:var(--text)}
.service-btn{width:112px;height:34px;line-height:34px;font-size:16px;top:2003px}
.dots{display:flex;gap:13px}
.dots i{width:7px;height:7px;border-radius:50%;background:#d8d8d8;display:block}
.dots i.on{background:var(--red)}

/* testimonial */
.testimonial{left:0;top:2150px;width:1200px;height:480px;background:linear-gradient(110deg,#232323 0%,#141414 40%,#262626 70%,#151515 100%)}
.quote-mark{left:0;top:2180px;width:1200px;text-align:center;font-family:var(--alt);font-size:80px;font-weight:600;color:var(--white);line-height:80px}
.quote-text{left:150px;top:2246px;width:900px;text-align:center;font-family:var(--alt);font-style:italic;font-size:25px;line-height:41px;color:var(--white)}
.avatar{left:552px;top:2399px;width:96px;height:96px;border-radius:50%;background:linear-gradient(#9a8f88,#d8cbbf);border:3px solid var(--white)}
.quote-name{left:0;top:2520px;width:1200px;text-align:center;font-size:19px;font-weight:600;color:var(--white);letter-spacing:.5px}

/* contact */
.field{border:1px solid var(--line);background:var(--white);font-family:var(--alt);font-size:17px;color:#8a8a8a;padding:18px 22px}
.submit{left:78px;top:2996px;width:131px;height:43px;line-height:43px;font-size:17px}
.address{left:867px;top:2757px;font-size:15px;line-height:34px;color:var(--text);letter-spacing:.5px}
.address strong{display:block;font-size:16px;color:var(--ink);font-weight:700}

/* footer */
.footer{left:0;top:3113px;width:1200px;height:451px;background:var(--dark)}
.footer-title{left:0;top:3165px;width:1200px;text-align:center;font-size:24px;font-weight:500;color:var(--white);letter-spacing:.5px}
.news-input{left:356px;top:3248px;width:400px;height:71px;border:1px solid #8a8a8a;color:var(--white);font-size:21px;padding:22px 38px;font-weight:500}
.news-btn{left:772px;top:3248px;width:71px;height:71px;background:var(--red)}
.social{top:3388px;width:58px;height:58px;border-radius:50%;background:var(--red)}
.copyright{left:0;top:3494px;width:1200px;text-align:center;font-size:17px;color:#d8d8d8}
</style>
</head>
<body>

<header class="abs site-nav">
  <div class="abs brand"><span class="brand-dot"></span>Silver Arch</div>
  <nav class="abs nav-links"><span>HOME</span><span>ABOUT</span><span>SERVICES</span><span>TESTIMONIALS</span><span>BOOKING</span><span>CONTACT</span></nav>
</header>

<section class="abs hero" role="img" aria-label="Photo of a business team meeting around a table, darkened"></section>
<h1 class="abs hero-title">IT'S GROW TIME</h1>
<p class="abs hero-text">From making strategic decisions to developing your capabilities, I'm here to help. Using my expertise and deep understanding of the industry, you'll receive real solutions and experience true results</p>
<div class="abs btn hero-btn">GET STARTED</div>

<p class="abs welcome-kicker">welcome to</p>
<p class="abs welcome-name">SILVER ARCH CONSULTING LLC</p>
<p class="abs welcome-text">We help owners and teams find clarity, build lasting habits, and grow with focus. Every plan is shaped around your goals, your people and your pace.</p>

<article class="abs offer" style="left:328px">
  <svg class="offer-icon" viewBox="0 0 56 56"><circle cx="28" cy="28" r="28" fill="#1d1d1d"/><rect x="17" y="22" width="22" height="16" rx="2" fill="none" stroke="#fff" stroke-width="2.4"/><path d="M23 22v-4h10v4" fill="none" stroke="#fff" stroke-width="2.4"/></svg>
  <h3>BUSINESS PERFORMANCE CONSULTING</h3>
  <p>By analyzing your systems, tools and people, I will identify strategies to get your business running at optimal efficiency. Book an introductory meeting today to learn more about how I can make your business thrive.</p>
</article>
<article class="abs offer is-featured" style="left:596px">
  <svg class="offer-icon" viewBox="0 0 56 56"><circle cx="28" cy="28" r="28" fill="#e0271a"/><circle cx="28" cy="28" r="12" fill="none" stroke="#fff" stroke-width="2.4"/><path d="M22 32l4-5 3 3 5-7" fill="none" stroke="#fff" stroke-width="2.4"/></svg>
  <h3>LEADERSHIP BUSINESS COACHING</h3>
  <p>Whether just starting out or looking to break through the invisible ceiling, we will work together on keeping you focused on the lead measures that will generate measurable results. Contact me to find out how I can help today.</p>
</article>
<article class="abs offer" style="left:862px">
  <svg class="offer-icon" viewBox="0 0 56 56"><circle cx="28" cy="28" r="28" fill="#1d1d1d"/><path d="M28 17c-7 0-12 4.5-12 10 0 3 1.5 5.5 4 7.2L19 40l6-3.3c1 .2 2 .3 3 .3 7 0 12-4.5 12-10s-5-10-12-10z" fill="none" stroke="#fff" stroke-width="2.2"/><circle cx="23" cy="27" r="1.6" fill="#fff"/><circle cx="28" cy="27" r="1.6" fill="#fff"/><circle cx="33" cy="27" r="1.6" fill="#fff"/></svg>
  <h3>SPEAKING AND TRAINING PACKAGE</h3>
  <p>Whether you need a single keynote or a training package for your organization, we will collaborate with you as a partner to design a package to train your team to the next level. To find out more, get in touch.</p>
</article>

<section class="abs about-panel"></section>
<h2 class="abs about-title">ABOUT ME?</h2>
<div class="abs about-rule"></div>
<p class="abs about-text">I've been a professional Business Coach since 2010. I believe in maintaining a positive mindset, creating partnerships with a purpose, and always striving for significant outcomes. When you work with me, you should expect a collaboration with transparency and consistency.</p>
<div class="abs about-btn">MORE</div>
<div class="abs about-video" role="img" aria-label="Video placeholder: two women talking across a table in a bright office"></div>
<svg class="abs play" viewBox="0 0 64 44"><rect width="64" height="44" rx="10" fill="#e0271a"/><path d="M26 13l15 9-15 9z" fill="#fff"/></svg>

<h2 class="abs section-title" style="top:1553px"><span>OUR</span> SERVICES</h2>

<article class="abs service" style="left:90px">
  <svg class="service-icon" viewBox="0 0 58 58"><circle cx="29" cy="29" r="28" fill="none" stroke="#1d1d1d" stroke-width="2"/><path d="M20 20h13a3 3 0 013 3v6a3 3 0 01-3 3h-7l-5 4v-4a3 3 0 01-3-3v-6a3 3 0 013-3z" fill="none" stroke="#1d1d1d" stroke-width="2"/><path d="M38 26h1a3 3 0 013 3v5a3 3 0 01-3 3v3l-4-3h-5" fill="none" stroke="#1d1d1d" stroke-width="2"/></svg>
  <h3>BUSINESS PERFORMANCE CONSULTATION</h3>
  <p>My clients are my number one priority, and my services prove just how committed I am to their success. Book an introductory meeting today to learn more about how I can make your business thrive</p>
</article>
<article class="abs service" style="left:345px">
  <svg class="service-icon" viewBox="0 0 58 58"><circle cx="29" cy="29" r="28" fill="none" stroke="#1d1d1d" stroke-width="2"/><path d="M29 15a9 9 0 00-5 16.5V36h10v-4.5A9 9 0 0029 15z" fill="none" stroke="#1d1d1d" stroke-width="2"/><path d="M25 40h8M26 43h6" stroke="#1d1d1d" stroke-width="2"/></svg>
  <h3>30 MINUTE STRATEGY SESSION</h3>
  <p>Looking to take your business, career and life to the next level? Let's have a conversation to see what opportunities exist within your unlocked potential</p>
</article>
<article class="abs service" style="left:606px">
  <svg class="service-icon" viewBox="0 0 58 58"><circle cx="29" cy="29" r="29" fill="#e0271a"/><rect x="25" y="15" width="8" height="16" rx="4" fill="#fff"/><path d="M21 27a8 8 0 0016 0M29 35v6M24 42h10" fill="none" stroke="#fff" stroke-width="2"/></svg>
  <h3 class="is-active">INTERACTIVE KEYNOTE ADDRESS</h3>
  <p>Looking for an engaging, interactive keynote address for you next event? Through our needs analysis process we will customize and personalize a motivating, entertaining talk especially for your group</p>
</article>
<article class="abs service" style="left:867px">
  <svg class="service-icon" viewBox="0 0 58 58"><circle cx="29" cy="29" r="28" fill="none" stroke="#1d1d1d" stroke-width="2"/><path d="M21 17l18 24M37 17l-16 24" stroke="#1d1d1d" stroke-width="2.4"/></svg>
  <h3>ENGAGING MASTERMIND LUNCH</h3>
  <p>Everyone has to eat! Let's grab lunch and talk shop.</p>
</article>

<div class="abs btn service-btn" style="left:90px">MORE</div>
<div class="abs btn service-btn" style="left:345px">MORE</div>
<div class="abs btn service-btn" style="left:606px">MORE</div>
<div class="abs btn service-btn" style="left:867px">MORE</div>
<div class="abs dots" style="left:570px;top:2092px"><i></i><i class="on"></i><i></i></div>

<section class="abs testimonial" role="img" aria-label="Darkened photo of business people at a networking event"></section>
<div class="abs quote-mark">&ldquo;</div>
<p class="abs quote-text">Daniel was my first mentor and trainer in real estate. He pushed me from nobody to rookie of the year international. He is that person who will bring the best out of you! I am forever grateful for his coaching and mentorship!</p>
<div class="abs avatar" role="img" aria-label="Portrait photo of the client"></div>
<p class="abs quote-name">OWEN HARTLEY</p>
<div class="abs dots" style="left:570px;top:2587px"><i></i><i class="on"></i><i></i></div>

<h2 class="abs section-title" style="top:2673px"><span>CONTACT</span> US</h2>
<div class="abs field" style="left:78px;top:2761px;width:281px;height:59px">First Name</div>
<div class="abs field" style="left:78px;top:2839px;width:281px;height:60px">Last Name</div>
<div class="abs field" style="left:78px;top:2915px;width:281px;height:60px">Email Address</div>
<div class="abs field" style="left:375px;top:2761px;width:457px;height:214px"></div>
<div class="abs btn submit">SUBMIT</div>
<address class="abs address" style="font-style:normal">
  <strong>ADDRESS:</strong>
  Jordan Ellery<br>P.O. Box 512 2207 Linden St.<br>Maple Grove Ohio 43210<br>(312) 555-0148
</address>

<footer class="abs footer"></footer>
<h2 class="abs footer-title">SUBSCRIBE FOR OUR NEWSLETTER</h2>
<div class="abs news-input">Email Address</div>
<svg class="abs news-btn" viewBox="0 0 71 71"><rect width="71" height="71" fill="#e0271a"/><path d="M21 36l10 10 20-22" fill="none" stroke="#fff" stroke-width="6" stroke-linecap="round" stroke-linejoin="round"/></svg>
<div class="abs social" style="left:280px" aria-label="Social link"></div>
<div class="abs social" style="left:422px" aria-label="Social link"></div>
<div class="abs social" style="left:567px" aria-label="Social link"></div>
<div class="abs social" style="left:712px" aria-label="Social link"></div>
<div class="abs social" style="left:857px" aria-label="Social link"></div>
<p class="abs copyright">&copy;2018 by Silver Arch Consulting LLC.</p>

</body>
</html>
```